Small local and internet boutique and custom sewing business that specializes in Custom cothing need

I work in the pagent industry making custom clothing rodeo and show clothing along with refinishing items like furniture and sell and customize items putting the customers own flare on them. I would like that put nicely across from to my customer I want my cards classy and fun shiney and cute. I live on a large ranch and have a cute studio in town were I am starting a boutique

Target Market(s)

women, horse show crowd pageant moms, rodeo queen moms and contestants, boutique shoppers, antique shoppers, ranchers

Industry/Entity Type

Business

Contact Information for Business Card

Colors

Requirements
Must have
• Corinne@Lacefernparlor.com
• Phone 482 319 6645
• Instagram Lacefernparlor
• Facebook www.facebook.com/Lacefernparlor.com
• Corinne Balfour (Whitcombe)
• Designer
• Fashion Forward Custom Clothing & Restyled Items

```html
<!DOCTYPE html>
<html lang="en">
<head>
<meta charset="utf-8">
<title>The Lacefern Parlor – Business Cards</title>
<link href="https://fonts.googleapis.com/css2?family=Marcellus&family=Josefin+Sans:wght@400&family=Montserrat:wght@400&display=swap" rel="stylesheet">
<style>
  :root {
    --paper: #ffffff;
    --ink: #141414;
    --gold: #c08a3a;
    --gold-light: #e6c27a;
    --gold-deep: #9a6a26;
    --cactus: #8fd068;
    --succulent: #8ec3a6;
    --shadow: rgba(0,0,0,0.22);
  }
  * { margin: 0; padding: 0; box-sizing: border-box; }
  html, body { width: 1200px; height: 1200px; overflow: hidden; background: var(--paper); }
  body { position: relative; font-family: "Montserrat", sans-serif; color: var(--ink); }

  .card {
    position: absolute;
    left: 182px;
    width: 838px;
    height: 475px;
    background: var(--paper);
    overflow: hidden;
    box-shadow: 0 6px 10px var(--shadow);
  }
  .card--front { top: 81px; }
  .card--back { top: 645px; }

  /* front artwork areas */
  .art { position: absolute; }
  .art--left {
    left: 0; top: 0; width: 170px; height: 475px;
    background: linear-gradient(180deg, var(--gold-light) 0%, #a9d77f 35%, var(--cactus) 65%, var(--gold-deep) 100%);
    border-radius: 0 60% 40% 0 / 0 50% 50% 0;
  }
  .art--right {
    right: 0; top: 0; width: 160px; height: 475px;
    background: linear-gradient(180deg, var(--gold-light) 0%, #a9d77f 30%, var(--cactus) 65%, var(--gold-deep) 100%);
    border-radius: 60% 0 0 40% / 50% 0 0 50%;
  }
  .art--top-succulent {
    left: 60px; top: -40px; width: 270px; height: 160px;
    background: radial-gradient(ellipse at center, #6fae8e 0%, var(--succulent) 60%, rgba(142,195,166,0.2) 100%);
    border-radius: 50%;
  }
  .art--bottom-succulent {
    left: 400px; top: 330px; width: 320px; height: 190px;
    background: radial-gradient(ellipse at center, #5fa585 0%, var(--succulent) 55%, rgba(142,195,166,0.15) 100%);
    border-radius: 50%;
  }

  .brand { position: absolute; left: 0; width: 100%; text-align: center; color: var(--gold); font-family: "Marcellus", serif; line-height: 1; transform: translateY(-50%); }
  .brand__rule { position: absolute; height: 2px; background: var(--gold); }

  .front .brand--the { top: 135px; font-size: 54px; }
  .front .brand--main { top: 203px; font-size: 96px; }
  .front .brand--sub { top: 276px; font-size: 56px; letter-spacing: 0.3em; padding-left: 0.3em; }
  .front .brand__rule--l { top: 274px; left: 166px; width: 66px; }
  .front .brand__rule--r { top: 274px; left: 606px; width: 66px; }

  /* back */
  .gold-frame { position: absolute; inset: 0; }
  .back .brand--the { top: 43px; font-size: 40px; }
  .back .brand--main { top: 92px; font-size: 68px; }
  .back .brand--sub { top: 143px; font-size: 40px; letter-spacing: 0.3em; padding-left: 0.3em; }
  .back .brand__rule--l { top: 142px; left: 240px; width: 48px; }
  .back .brand__rule--r { top: 142px; left: 550px; width: 48px; }

  .tagline { position: absolute; top: 174px; left: 0; width: 100%; text-align: center; font-size: 13.5px; letter-spacing: 0.02em; transform: translateY(-50%); }
  .person__name { position: absolute; top: 275px; left: 0; width: 100%; text-align: center; font-family: "Josefin Sans", sans-serif; font-variant: small-caps; font-size: 38px; letter-spacing: 0.06em; transform: translateY(-50%); }
  .person__role { position: absolute; top: 310px; left: 0; width: 100%; text-align: center; font-family: "Josefin Sans", sans-serif; font-size: 17px; letter-spacing: 0.55em; padding-left: 0.55em; transform: translateY(-50%); }

  .contact { position: absolute; left: 0; width: 100%; display: flex; justify-content: center; align-items: center; gap: 10px; font-size: 20px; transform: translateY(-50%); }
  .contact--primary { top: 399px; }
  .contact--social { top: 431px; }
  .contact__sep { margin: 0 10px; }
  .contact__icon { width: 26px; height: 22px; flex: none; }
  .contact__mark { width: 24px; height: 24px; flex: none; background: var(--gold); border-radius: 5px; }
</style>
</head>
<body>

<section class="card card--front front">
  <div class="art art--left" role="img" aria-label="Watercolour prickly pear cactus over gold glitter"></div>
  <div class="art art--right" role="img" aria-label="Watercolour cactus and sprigs over gold glitter"></div>
  <div class="art art--top-succulent" role="img" aria-label="Watercolour succulent rosette"></div>
  <div class="art art--bottom-succulent" role="img" aria-label="Watercolour succulent rosette"></div>

  <div class="brand brand--the">THE</div>
  <div class="brand brand--main">LACEFERN</div>
  <span class="brand__rule brand__rule--l"></span>
  <div class="brand brand--sub">PARLOR</div>
  <span class="brand__rule brand__rule--r"></span>
</section>

<section class="card card--back back">
  <svg class="gold-frame" width="838" height="475" viewBox="0 0 838 475" role="img" aria-label="Gold glitter edges framed by curved arcs">
    <defs>
      <linearGradient id="glitter" x1="0" y1="0" x2="0" y2="1">
        <stop offset="0" stop-color="#e7c27c"/>
        <stop offset="0.55" stop-color="#d2a253"/>
        <stop offset="1" stop-color="#a8722a"/>
      </linearGradient>
    </defs>
    <rect width="838" height="475" fill="url(#glitter)"/>
    <ellipse cx="419" cy="237" rx="407" ry="339" fill="#ffffff"/>
    <ellipse cx="419" cy="237" rx="375" ry="322" fill="none" stroke="#c8963f" stroke-width="3"/>
  </svg>

  <div class="brand brand--the">THE</div>
  <div class="brand brand--main">LACEFERN</div>
  <span class="brand__rule brand__rule--l"></span>
  <div class="brand brand--sub">PARLOR</div>
  <span class="brand__rule brand__rule--r"></span>

  <p class="tagline">CUSTOM RODEO-SHOW CLOTHING &amp; ITEM REFINISHING</p>

  <p class="person__name">Corinne Balfour</p>
  <p class="person__role">DESIGNER</p>

  <div class="contact contact--primary">
    <svg class="contact__icon" viewBox="0 0 26 20" aria-hidden="true">
      <rect x="1" y="1" width="24" height="18" fill="#d9a55a"/>
      <path d="M1 1 L13 11 L25 1 M1 19 L10 9 M25 19 L16 9" fill="none" stroke="#fff" stroke-width="1.6"/>
    </svg>
    <span>corinne@lacefernparlor.com</span>
    <span class="contact__sep">|</span>
    <span>482 319 6645</span>
    <svg class="contact__icon" viewBox="0 0 24 24" aria-hidden="true">
      <path d="M6.6 2.5 L9.5 6.8 L7.6 9.2 C8.8 11.8 11.2 14.2 14.1 15.6 L16.4 13.7 L21 16.5 L19.6 20.4 C12 20.8 3.6 12.6 3 4.2 Z" fill="#c8903e"/>
    </svg>
  </div>

  <div class="contact contact--social">
    <span class="contact__mark" aria-hidden="true"></span>
    <span>@lacefernparlor</span>
    <span class="contact__sep">|</span>
    <span>Lacefernparlor</span>
    <span class="contact__mark" aria-hidden="true"></span>
  </div>
</section>

</body>
</html>
```